Vorental d.o.o. needes a web site design

We are a company dealing with automatic doors, industrial doors, roller shutters, access control systems.
We would like to get a design which is clean and neat, and here are some sites which work with similar products. These designs are some we like, but of course, I am looking for a design which is unique. We usually use grey and red colours, which you can see on www.vorental.ba .
The sites we like are:
http://www.plinsta.com/gb/
http://www.bravidosteel.it/eng/
http://morrowpanelgate.com/

You have to understand, that we have 4 different groups of products, which are main groups. I would like if those 4 groups somehow could be in different colours. (Maybe "zenpoq" colours), in order to separate the groups in some way.

Attached you have web site structure.

If any questions, please contact me.
Edvan

Target Market(s)

Bosnian market. Aluminium and PVC doors and window market, Construction companies, Supermarkets-Retail, Gas stations, Banks, Food industry, Heavy industry.

Industry/Entity Type

It Company

Contact Information for Business Card

I have attached our current business card in PDF. I weould like english on one side, bosnian on other side.

Logo Text

Vorental is the name of the company, our core business is automation!

Number of Pages Required

5+ page

Font styles to use
Sans Serif

Colors
ec1f27
0792cd
9bcb3c
ffc214
ffffff

```html
<!DOCTYPE html>
<html lang="en">
<head>
<meta charset="utf-8">
<title>Vorental d.o.o.</title>
<link rel="stylesheet" href="https://fonts.googleapis.com/css2?family=Muli:wght@400;600;700&family=Open+Sans:wght@400;600&family=Ubuntu:wght@400;500&display=swap">
<style>
:root{
  --red:#ec1f27;
  --blue:#0792cd;
  --green:#9bcb3c;
  --yellow:#ffc214;
  --white:#ffffff;
  --ink:#222222;
  --muted:#666666;
  --rule:#c8c8c8;
  --panel:#ececec;
  --slate:#58585a;
}
*{margin:0;padding:0;box-sizing:border-box}
html,body{width:742px;height:1200px;overflow:hidden;background:var(--white)}
body{font-family:"Open Sans",sans-serif;color:var(--ink)}
.page{position:relative;width:742px;height:1200px;overflow:hidden}
.abs{position:absolute}

/* header */
.site-header{left:0;top:0;width:742px;height:70px;background:var(--white)}
.contact{top:29px;font-size:8px;color:var(--muted)}
.contact.email{left:88px}
.contact.phone{left:517px}
.brand{left:290px;top:0;width:170px;height:70px;display:flex;align-items:center;justify-content:center;gap:7px;box-shadow:0 0 3px rgba(0,0,0,.08)}
.brand-mark{width:12px;height:12px;background:var(--red)}
.brand-name{font-family:"Muli",sans-serif;font-weight:700;font-size:18px;color:var(--red)}

/* hero */
.hero{left:0;top:70px;width:742px;height:365px;background:linear-gradient(90deg,#1c1c1c 0%,#4a4a4a 35%,#3a3a3a 60%,#2a2a2a 100%)}
.hero-title{left:0;top:129px;width:742px;text-align:center;font-family:"Ubuntu",sans-serif;font-weight:500;font-size:35px;color:var(--white);letter-spacing:.5px}
.hero-sub{left:0;top:179px;width:742px;text-align:center;font-family:"Ubuntu",sans-serif;font-size:12.5px;line-height:17px;color:var(--white)}
.btn{display:flex;align-items:center;justify-content:center;font-size:7.5px;color:var(--white);background:var(--red)}
.hero .btn{left:329px;top:231px;width:84px;height:26px;border:1px solid var(--white);border-radius:3px}
.slider-nav{left:354px;top:346px;width:41px;height:19px;background:#d8d8d8}

/* welcome */
.welcome{left:0;top:435px;width:742px;height:179px;background:var(--panel)}
.welcome-title{left:0;top:27px;width:742px;text-align:center;font-family:"Muli",sans-serif;font-weight:600;font-size:22px;color:var(--ink)}
.welcome-title span{color:var(--red)}
.rule{height:1px;background:var(--rule);top:41px}
.rule.l{left:29px;width:180px}
.rule.r{left:531px;width:181px}
.welcome-text{left:80px;top:69px;width:582px;text-align:center;font-size:7.2px;line-height:14px;color:var(--muted)}
.welcome .btn{left:331px;top:126px;width:80px;height:24px;border-radius:2px}

/* products */
.products{left:0;top:614px;width:742px;height:337px;background:var(--white)}
.section-title{left:0;width:742px;text-align:center;font-family:"Muli",sans-serif;font-weight:600}
.products .section-title{top:22px;font-size:21px}
.products .section-title span{color:var(--red)}
.product-row{left:0;top:69px}
.product-label{font-family:"Muli",sans-serif;font-weight:600;font-size:11px;fill:var(--white)}

/* testimonials */
.testimonials{left:0;top:951px;width:742px;height:206px;background:var(--slate)}
.testimonials .section-title{top:28px;font-size:21px;color:var(--white)}
.quote{left:140px;top:88px;width:490px;text-align:center;font-size:8px;line-height:18px;color:var(--white)}
.quote-mark{font-family:"Ubuntu",sans-serif;font-size:16px;font-style:italic;line-height:0}
.author{left:0;top:134px;width:742px;text-align:center;font-size:10px;color:var(--white)}
.dots{left:0;top:167px;width:742px;display:flex;justify-content:center;align-items:center;gap:7px}
.dot{width:6px;height:6px;border-radius:50%;background:var(--white)}
.dot.active{width:9px;height:9px;background:transparent;border:2px solid var(--white)}

/* footer */
.site-footer{left:0;top:1157px;width:742px;height:43px;background:var(--white)}
.copyright{left:29px;top:17px;font-size:7px;color:#444}
.social{left:606px;top:19px;display:flex;gap:15px}
.social i{display:block;width:8px;height:8px;border-radius:50%;background:#555}
.social i:first-child{background:var(--red)}
</style>
</head>
<body>
<div class="page">

  <header class="site-header abs">
    <div class="contact email abs">Email id : info@vorental-mail.ba</div>
    <div class="brand abs"><span class="brand-mark"></span><span class="brand-name">Vorental d.o.o.</span></div>
    <div class="contact phone abs">Call Us : 033-555-0142</div>
  </header>

  <section class="hero abs" role="img" aria-label="Blurred black-and-white photo of people walking through a busy hall">
    <h1 class="hero-title abs">NOVA WEB STRANICA</h1>
    <p class="hero-sub abs">u toku su radovi na novoj web prezentaciji naših usluga,<br>uskoro smo ponovo sa vama</p>
    <a class="btn abs">READ MORE</a>
    <div class="slider-nav abs">
      <svg width="41" height="19" viewBox="0 0 41 19"><path d="M16 6l-4 3.5 4 3.5M25 6l4 3.5-4 3.5" fill="none" stroke="#222" stroke-width="1.4"/></svg>
    </div>
  </section>

  <section class="welcome abs">
    <div class="rule l abs"></div>
    <h2 class="welcome-title abs">Welcome to <span>Vorental</span></h2>
    <div class="rule r abs"></div>
    <p class="welcome-text abs">Lorem ipsum dolor sit amet, consectetur adipiscing elit, sed do eiusmod tempor incididunt ut labore et dolore magna aliqua. Ut enim ad minim veniam, quis nostrud exercitation ullamco laboris nisi ut aliquip ex ea commodo consequat. Duis aute irure dolor in reprehenderit in voluptate velit esse cillum dolore eu fugiat nulla pariatur. Excepteur sint occaecat cupidatat non proident, sunt in culpa qui officia deserunt mollit anim id est laborum.</p>
    <a class="btn abs">READ MORE</a>
  </section>

  <section class="products abs">
    <h2 class="section-title abs">Our <span>Product</span></h2>
    <svg class="product-row abs" width="742" height="220" viewBox="0 0 742 220">
      <defs>
        <linearGradient id="g-auto" x1="0" y1="0" x2="0" y2="1"><stop offset="0" stop-color="#c9c4bb"/><stop offset="1" stop-color="#8f8a80"/></linearGradient>
        <linearGradient id="g-ind" x1="0" y1="0" x2="1" y2="0"><stop offset="0" stop-color="#6f7d8c"/><stop offset=".5" stop-color="#2057a8"/><stop offset="1" stop-color="#8a9aa8"/></linearGradient>
        <linearGradient id="g-roll" x1="0" y1="0" x2="0" y2="1"><stop offset="0" stop-color="#5a5fc9"/><stop offset="1" stop-color="#3a3fae"/></linearGradient>
        <linearGradient id="g-acc" x1="0" y1="0" x2="1" y2="1"><stop offset="0" stop-color="#6d7c8e"/><stop offset="1" stop-color="#2f3740"/></linearGradient>
      </defs>
      <g role="img" aria-label="Photo of an automatic revolving glass door">
        <polygon points="56,0 217,0 190,219 29,219" fill="url(#g-auto)"/>
        <polygon points="38,162 192,162 187,201 31,201" fill="var(--red)"/>
        <text class="product-label" x="110" y="186" text-anchor="middle">Automatic Doors</text>
      </g>
      <g role="img" aria-label="Photo of a blue industrial sectional door">
        <polygon points="226,0 382,0 351,219 194,219" fill="url(#g-ind)"/>
        <polygon points="203,162 359,162 354,201 198,201" fill="var(--blue)"/>
        <text class="product-label" x="276" y="186" text-anchor="middle">Industrial Doors</text>
      </g>
      <g role="img" aria-label="Photo of a closed purple roller shutter">
        <polygon points="390,0 548,0 516,219 360,219" fill="url(#g-roll)"/>
        <polygon points="368,162 543,162 538,201 363,201" fill="var(--green)"/>
        <text class="product-label" x="440" y="186" text-anchor="middle">Roller Shutters</text>
      </g>
      <g role="img" aria-label="Photo of an access control card reader with an ID card">
        <polygon points="554,0 712,0 680,219 530,219" fill="url(#g-acc)"/>
        <polygon points="531,162 687,162 682,201 526,201" fill="var(--yellow)"/>
        <text class="product-label" x="604" y="186" text-anchor="middle">Access Control Systems</text>
      </g>
    </svg>
  </section>

  <section class="testimonials abs">
    <h2 class="section-title abs">Client Testimonials</h2>
    <p class="quote abs"><span class="quote-mark">“</span> Lorem ipsum dolor sit amet, consectetur adipiscing elit, sed do eiusmod tempor incididunt ut labore et dolore magna aliqua.<br>Ut enim ad minim veniam, quis nostrud exercitation ullamco laboris.<span class="quote-mark">”</span></p>
    <p class="author abs">- JARON VELK</p>
    <div class="dots abs"><span class="dot"></span><span class="dot active"></span><span class="dot"></span></div>
  </section>

  <footer class="site-footer abs">
    <p class="copyright abs">All Rights Reserved. Copyrights @Vorental d.o.o. 2016</p>
    <div class="social abs"><i></i><i></i><i></i><i></i><i></i></div>
  </footer>

</div>
</body>
</html>
```